furnace plenum sticker

This sticker is left at every job above the furnace or on the duct work connected to the furnace.
It needs to be bold so that when homeowner is at the furnace during a break down they see it. Phone number and what we do needs to be prominate. It is our calling card for service.
Sticker needs to look corporate and professional.

New logo (attached) must be incorporated into sticker.

Current sticker attached
Size
8.5 inches x 5.5 inches

Target Market(s)

residential home owners

Industry/Entity Type

Work

Colors
ec1f27

Requirements
Must have
• Our new current logo attached

```html
<!DOCTYPE html>
<html lang="en">
<head>
<meta charset="utf-8">
<title>Northgate Heating and Air Conditioning – Furnace Sticker</title>
<link href="https://fonts.googleapis.com/css2?family=Arimo:wght@700&display=swap" rel="stylesheet">
<style>
  :root {
    --brand-red: #ec1f27;
    --ink: #231f20;
    --paper: #ffffff;
    --blush: #f6b9a3;
  }
  html, body {
    margin: 0;
    padding: 0;
    width: 1200px;
    height: 1000px;
    overflow: hidden;
    background: var(--paper);
    font-family: "Arimo", Arial, sans-serif;
  }
  .sticker {
    position: absolute;
    left: 88px;
    top: 204px;
    width: 1020px;
    height: 588px;
    border: 2px solid var(--ink);
    background: linear-gradient(to bottom,
      var(--paper) 0%, var(--paper) 47%,
      var(--blush) 66%, #ee7a62 88%, var(--brand-red) 100%);
    overflow: hidden;
  }
  .brand-name {
    position: absolute;
    left: 0;
    right: 0;
    top: 78px;
    margin: 0;
    text-align: center;
    font-weight: 700;
    font-size: 104px;
    line-height: 1;
    letter-spacing: 2px;
    color: var(--brand-red);
  }
  .trade-line {
    position: absolute;
    left: 0;
    right: 0;
    top: 206px;
    margin: 0;
    text-align: center;
    font-weight: 700;
    font-size: 45px;
    line-height: 1;
    letter-spacing: 1px;
    color: var(--ink);
  }
  .phone-pill {
    position: absolute;
    left: 264px;
    width: 496px;
    height: 92px;
    border: 2px solid var(--paper);
    border-radius: 46px;
    background: var(--brand-red);
    box-shadow: 0 4px 12px rgba(236, 31, 39, 0.45);
    text-align: center;
    color: var(--ink);
  }
  .phone-pill.burlington { top: 280px; }
  .phone-pill.oakville { top: 402px; }
  .phone-pill .area {
    display: block;
    margin-top: 8px;
    font-size: 24px;
    line-height: 1;
    letter-spacing: 0.5px;
  }
  .phone-pill .number {
    display: block;
    margin-top: 4px;
    font-size: 52px;
    line-height: 1;
    letter-spacing: 1px;
  }
  .service-clock {
    position: absolute;
    left: 796px;
    top: 316px;
    width: 190px;
    height: 170px;
  }
  .service-clock svg {
    position: absolute;
    left: 0;
    top: 0;
  }
  .service-clock .hours {
    position: absolute;
    left: 4px;
    top: 46px;
    font-size: 60px;
    line-height: 1;
    color: var(--ink);
    letter-spacing: -1px;
  }
  .service-clock .hours small {
    font-size: 44px;
  }
  .service-clock .label {
    position: absolute;
    left: 4px;
    top: 110px;
    font-size: 24px;
    line-height: 1;
    color: var(--ink);
  }
  .tagline {
    position: absolute;
    left: 0;
    right: 0;
    top: 540px;
    margin: 0;
    text-align: center;
    font-size: 23px;
    line-height: 1;
    letter-spacing: 0.5px;
    color: var(--ink);
  }
</style>
</head>
<body>
  <main class="sticker">
    <h1 class="brand-name">NORTHGATE INC.</h1>
    <p class="trade-line">HEATING AND AIR CONDITIONING</p>

    <div class="phone-pill burlington">
      <span class="area">BURLINGTON / HAMILTON</span>
      <span class="number">905-555-0142</span>
    </div>
    <div class="phone-pill oakville">
      <span class="area">OAKVILLE / MISSISSAUGA</span>
      <span class="number">905-555-0187</span>
    </div>

    <div class="service-clock">
      <svg width="190" height="170" viewBox="0 0 190 170" aria-hidden="true">
        <path d="M33 40 A78 78 0 1 1 80 163" fill="none" stroke="#231f20" stroke-width="9" stroke-linecap="butt"/>
        <rect x="98" y="18" width="3" height="12" fill="#231f20"/>
        <rect x="98" y="139" width="3" height="12" fill="#231f20"/>
        <rect x="160" y="83" width="12" height="3" fill="#231f20"/>
        <circle cx="131" cy="28" r="2" fill="#231f20"/>
        <circle cx="155" cy="52" r="2" fill="#231f20"/>
        <circle cx="155" cy="117" r="2" fill="#231f20"/>
        <circle cx="131" cy="141" r="2" fill="#231f20"/>
        <circle cx="66" cy="28" r="2" fill="#231f20"/>
      </svg>
      <div class="hours">24<small>H</small></div>
      <div class="label">SERVICE</div>
    </div>

    <p class="tagline">We service all makes and models. Repairs and Installations.</p>
  </main>
</body>
</html>
```